Business card design for Plumbing and Gas fitting company

We need a business card design for our plumbing and gas fitting company using the company logo and director details. Design should be modern and eye-catching however kept reasonably simple. This design should be targeted at commercial businesses/work so professionalism is key.

Target Market(s)

Commercial/business

Industry/Entity Type

Plumbing

Contact Information for Business Card

Warren Dohey
Director
027 581 9043
warren@vantorplumbingandgas.example
PO Box 7816
Palmerston North 4472

Font styles to use
Sans Serif

Requirements
Must have
• Logo
• Modern
• Kept simple
Nice to have
• Colour scheme based around logo

```html
<!DOCTYPE html>
<html lang="en">
<head>
<meta charset="utf-8">
<title>Vantor Plumbing &amp; Gas — Business Cards</title>
<link rel="stylesheet" href="https://fonts.googleapis.com/css2?family=Quicksand:wght@500;700&display=swap">
<style>
  :root {
    --page-bg: #eceaf3;
    --card-dark: #1c1c1f;
    --brand-blue: #1577c4;
    --wave-grey-deep: #3b3b3f;
    --wave-grey-light: #4a4a4f;
    --text-white: #ffffff;
    --text-grey: #8e8e93;
    --accent-orange: #ee7a2a;
  }
  * { box-sizing: border-box; margin: 0; padding: 0; }
  html, body {
    width: 1200px; height: 900px; overflow: hidden;
    background: var(--page-bg);
    font-family: "Quicksand", sans-serif;
  }
  .canvas { position: relative; width: 1200px; height: 900px; }
  .card {
    position: absolute;
    background: var(--card-dark);
    border-radius: 22px;
    overflow: hidden;
    box-shadow: 0 18px 40px rgba(40, 40, 70, 0.18);
  }

  /* Front: brand face, portrait */
  .card-front { left: 140px; top: 170px; width: 320px; height: 560px; }
  .front-decor-area {
    position: absolute; left: 0; bottom: 0; width: 320px; height: 130px;
    background: linear-gradient(180deg, var(--card-dark) 0%, var(--wave-grey-light) 45%, var(--wave-grey-deep) 100%);
  }
  .front-brand {
    position: absolute; left: 0; right: 0; top: 190px;
    display: flex; flex-direction: column; align-items: center; gap: 18px;
  }
  .brand-mark {
    width: 26px; height: 26px; border-radius: 50%;
    background: var(--accent-orange);
  }
  .front-brand .brand-name {
    color: var(--brand-blue);
    font-weight: 700; font-size: 30px; line-height: 1.15;
    text-align: center;
  }

  /* Back: contact face, landscape */
  .card-back { left: 520px; top: 290px; width: 560px; height: 320px; }
  .card-back .band { position: absolute; inset: 0; width: 560px; height: 320px; }
  .holder { position: absolute; left: 38px; top: 30px; }
  .holder-name {
    color: var(--brand-blue); font-weight: 700; font-size: 28px; letter-spacing: 0.5px;
  }
  .holder-role {
    color: var(--text-grey); font-weight: 500; font-size: 14px; margin-top: 2px;
  }
  .contact-list {
    position: absolute; left: 38px; top: 118px;
    list-style: none; color: var(--text-white);
    font-weight: 700; font-size: 14px; line-height: 1.65;
  }
  .contact-list .email { font-weight: 500; font-size: 13px; }
  .back-brand {
    position: absolute; right: 30px; bottom: 30px;
    display: flex; align-items: center; gap: 8px;
  }
  .back-brand .brand-name {
    color: var(--text-grey); font-weight: 700; font-size: 15px;
  }
  .back-brand .brand-mark { width: 14px; height: 14px; }
</style>
</head>
<body>
<main class="canvas">

  <section class="card card-front" aria-label="Business card front">
    <div class="front-brand">
      <span class="brand-name">Vantor<br>Plumbing &amp; Gas</span>
      <span class="brand-mark" aria-hidden="true"></span>
    </div>
    <div class="front-decor-area" role="img" aria-label="Decorative grey wave ornament along the bottom edge"></div>
  </section>

  <section class="card card-back" aria-label="Business card back">
    <svg class="band" viewBox="0 0 560 320" aria-hidden="true">
      <path d="M0 100 H440 V150 C440 198 402 206 362 216 C322 226 300 250 290 272 H0 Z" fill="var(--brand-blue)"/>
      <line x1="0" y1="96" x2="560" y2="96" stroke="var(--brand-blue)" stroke-width="2"/>
    </svg>
    <div class="holder">
      <p class="holder-name">Warren Dohey</p>
      <p class="holder-role">Director</p>
    </div>
    <ul class="contact-list">
      <li>027 581 9043</li>
      <li class="email">warren@vantorplumbingandgas.example</li>
      <li>PO Box 7816</li>
      <li>Palmerston North 4472</li>
    </ul>
    <div class="back-brand">
      <span class="brand-name">Vantor Plumbing &amp; Gas</span>
      <span class="brand-mark" aria-hidden="true"></span>
    </div>
  </section>

</main>
</body>
</html>
```